business card for LWR pty ltd

We require a business card that stands out . I have included our company flyer and would like the services listed to be put on the card so when we Give out the cards to customers they have an idea of services we provide. need the winning design to be in editable photo shop format, editable iMac pages format or editable windows publisher format, so that I can enter in names, email addresses, phone numbers etc myself. I have included a pdf documents of info / items needed on the card to use as reference please.
Updates

need more submissions

Need extra days to review

Sick

Target Market(s)

new customers

Contact Information for Business Card

details are on attached business card requirements file

Requirements
Must have
• I have attached a list of must haves

```html
<!DOCTYPE html>
<html lang="en">
<head>
<meta charset="utf-8">
<title>LWR pty ltd – Business Card</title>
<link href="https://fonts.googleapis.com/css2?family=Roboto:wght@400;500;700;900&display=swap" rel="stylesheet">
<style>
  :root{
    --stage:#1b1b1d;
    --card-dark:#221d1a;
    --black:#0b0b0b;
    --gold:#a0823f;
    --gold-light:#c9a65a;
    --gold-text:#b89550;
    --white:#f4f1ea;
    --earth-1:#c98a55;
    --earth-2:#a8683b;
    --chrome:#d7d9dc;
  }
  *{box-sizing:border-box;margin:0;padding:0}
  html,body{width:1200px;height:900px;overflow:hidden}
  body{
    background:var(--stage);
    font-family:"Roboto",Arial,sans-serif;
    display:flex;flex-direction:column;align-items:center;justify-content:center;gap:40px;
  }
  .card{width:700px;height:400px;position:relative;overflow:hidden;box-shadow:0 12px 30px rgba(0,0,0,.5)}

  /* Services side */
  .card--services{background:var(--black)}
  .services__texture{
    position:absolute;left:0;top:0;width:100%;height:110px;
    background:linear-gradient(180deg,#050505 0%,#1c1c1e 100%);
  }
  .services__photo{
    position:absolute;left:0;top:40px;width:100%;height:240px;
    background:linear-gradient(180deg,#2a2a2c 0%,#4a3a2c 38%,var(--earth-1) 60%,var(--earth-2) 100%);
  }
  .services__brand{
    position:absolute;right:40px;top:18px;
    font-weight:900;font-size:96px;letter-spacing:4px;line-height:1;color:var(--chrome);
  }
  .services__band{
    position:absolute;left:0;bottom:0;width:100%;height:120px;
    background:var(--gold);border-bottom:8px solid var(--gold-light);
    display:flex;flex-direction:column;justify-content:center;align-items:flex-end;
    padding:0 28px;gap:3px;
  }
  .services__line{color:var(--white);font-size:15px;line-height:1.2;white-space:nowrap}

  /* Contact side */
  .card--contact{background:var(--card-dark)}
  .contact__details{position:absolute;left:46px;top:44px}
  .contact__name{color:var(--gold-text);font-weight:700;font-size:26px;text-transform:uppercase;letter-spacing:.5px}
  .contact__role{color:var(--white);font-size:17px;margin-top:4px}
  .contact__company{color:var(--gold-text);font-size:19px;margin-top:32px}
  .contact__address{color:var(--white);font-size:17px;line-height:1.35;margin-top:4px}
  .contact__list{list-style:none;margin-top:16px}
  .contact__item{display:flex;align-items:center;gap:9px;color:var(--white);font-size:17px;line-height:1.45}
  .contact__icon{width:14px;height:14px;fill:var(--gold-text);flex:none}
  .contact__photo{
    position:absolute;right:0;bottom:0;width:390px;height:250px;
    background:radial-gradient(ellipse at 55% 60%,#6b625a 0%,#3e3833 45%,var(--card-dark) 75%);
  }
</style>
</head>
<body>

  <section class="card card--services">
    <div class="services__texture"></div>
    <div class="services__photo" role="img" aria-label="Road train truck with tipper trailers on red outback dirt"></div>
    <div class="services__brand">LWR</div>
    <div class="services__band">
      <p class="services__line">Over Size Loads / Hot Shot Loads / Heavy Vehicle Recovery Services</p>
      <p class="services__line">Potable Water Deliveries / Road, Building / Mamaintenance / Earthworks</p>
      <p class="services__line">Sand &amp; Metal Supply &amp; Cartage / Road Train Tippers / Road Train Trankers</p>
      <p class="services__line">Road Train Flat Tops / Drop Deck Trailers / Mine Site accredited equipment &amp; Operators</p>
    </div>
  </section>

  <section class="card card--contact">
    <div class="contact__photo" role="img" aria-label="Front view of a road train prime mover with bull bar"></div>
    <div class="contact__details">
      <h1 class="contact__name">Daniel Corbett</h1>
      <p class="contact__role">Director</p>
      <p class="contact__company">LWR pty ltd</p>
      <p class="contact__address">Depot: Lot 444<br>example address Australia</p>
      <ul class="contact__list">
        <li class="contact__item">
          <svg class="contact__icon" viewBox="0 0 24 24"><path d="M6.6 10.8a15.1 15.1 0 0 0 6.6 6.6l2.2-2.2a1 1 0 0 1 1-.25 11.4 11.4 0 0 0 3.6.6 1 1 0 0 1 1 1V20a1 1 0 0 1-1 1A17 17 0 0 1 3 4a1 1 0 0 1 1-1h3.5a1 1 0 0 1 1 1c0 1.25.2 2.45.6 3.6a1 1 0 0 1-.25 1z"/></svg>
          000 444 000
        </li>
        <li class="contact__item">
          <svg class="contact__icon" viewBox="0 0 24 24"><path d="M2 5h20v14H2z M2 5l10 8 10-8" stroke="#221d1a" stroke-width="1.5"/></svg>
          email@lwrhaulage.com.au
        </li>
        <li class="contact__item">
          <svg class="contact__icon" viewBox="0 0 24 24"><circle cx="12" cy="12" r="10"/><path d="M2 12h20M12 2c3 3 3 17 0 20M12 2c-3 3-3 17 0 20" stroke="#221d1a" stroke-width="1.5" fill="none"/></svg>
          www.websiteaddress.com
        </li>
      </ul>
    </div>
  </section>

</body>
</html>
```